A modern web page for a software product

We need a web page for a software product, which is an advanced solution based on Machine Learning and Natural Language processing. We already have a logo of the product and expect the web page to be inline with the logo colors. The design should be for one page web site with scrolled sections - details of the content and guidelines in the attachments.

Target Market(s)

software company

Industry/Entity Type

It Company

Number of Pages Required

1 page

Colors

Designer to choose colors to be used in the design.

Requirements
Must have
• - modern icons and graphics
• - inline with the logo colors
• - be related to Machine Learining, AI, data processing
• - should have two language versions: english and polish both are attached.
Nice to have
• - animation/motion
Should not have
• - any photos embedded

```html
<!DOCTYPE html>
<html lang="en">
<head>
<meta charset="utf-8">
<title>PRODXYZ for GDPR</title>
<link href="https://fonts.googleapis.com/css2?family=Roboto:wght@400;500;700&display=swap" rel="stylesheet">
<style>
:root{
  --teal:#2bb5d4;
  --blue:#1e97cf;
  --navy:#1a2a44;
  --navy-deep:#101d31;
  --ink:#1f2a36;
  --text:#3a4652;
  --link-blue:#1e5f8e;
  --pale:#e8f8fd;
  --pale-row:#c9ecf8;
  --line:#d7dde2;
  --header-bg:#f3f4f5;
}
*{box-sizing:border-box;margin:0;padding:0}
html,body{width:1200px;height:2691px;overflow:hidden}
body{font-family:"Roboto",Arial,sans-serif;color:var(--text);background:#fff;position:relative}

/* header */
.site-header{position:absolute;top:0;left:0;width:1200px;height:72px;background:var(--header-bg)}
.brand{position:absolute;left:86px;top:18px;display:flex;align-items:center;gap:10px;font-weight:700;font-size:28px;color:var(--navy)}
.brand-dot{width:14px;height:14px;border-radius:50%;background:var(--teal)}
.main-nav a{position:absolute;top:28px;font-size:15px;color:var(--ink);text-decoration:none;letter-spacing:.3px}
.main-nav a.active::after{content:"";position:absolute;left:-4px;right:-4px;top:40px;height:3px;background:var(--teal)}

/* hero */
.hero{position:absolute;top:72px;left:0;width:1200px;height:525px}
.hero-art{position:absolute;inset:0;background:radial-gradient(ellipse at 62% 45%,#2d4a5e 0%,#14222f 45%,#0a121a 100%)}
.hero-title{position:absolute;left:86px;top:222px;font-size:43px;font-weight:700;color:#fff;letter-spacing:.5px}
.hero-sub{position:absolute;left:86px;top:276px;font-size:25px;font-weight:500;color:#fff}
.hero-arrow{position:absolute;top:238px}

/* headings */
.section-title{position:absolute;left:0;width:1200px;text-align:center;font-size:26px;font-weight:700;color:var(--ink)}
.section-title::after{content:"";position:absolute;left:570px;width:60px;height:2px;background:var(--blue);top:42px}
.on-dark{color:#fff}

/* features */
.feature-list{position:absolute;left:86px;top:719px;width:596px;list-style:none}
.feature-head{height:49px;background:var(--blue);color:#fff;font-size:16px;display:flex;align-items:center;padding-left:16px}
.feature-detail{background:var(--pale);height:142px;padding:10px 0 0 14px;list-style:none}
.feature-detail li{font-size:13.5px;color:var(--ink);height:31px;line-height:31px}
.feature-detail li::before{content:"› ";color:var(--text)}
.feature-item{height:49px;background:var(--pale-row);color:var(--link-blue);font-size:16px;display:flex;align-items:center;padding-left:16px;margin-top:6px}
.feature-visual{position:absolute;left:700px;top:719px;width:414px;height:521px;background:var(--blue)}
.feature-visual .art{position:absolute;left:18px;top:17px;right:0;bottom:0;background:linear-gradient(160deg,#3a4f68 0%,#c9d0db 45%,#1f2f49 100%)}

/* use cases */
.case-list{position:absolute;left:86px;top:1354px;width:1026px;list-style:none}
.case{display:flex;align-items:center;border:1px solid var(--line);background:#fff;margin-bottom:9px}
.case-icon{width:72px;align-self:stretch;background:var(--teal);display:flex;align-items:center;justify-content:center;flex:none}
.case-text{padding-left:22px;font-size:14px;color:var(--ink);line-height:24px}
.tag{display:inline-flex;align-items:center;gap:5px;margin-right:22px;font-size:12.5px}
.tag::before{content:"›";display:inline-flex;align-items:center;justify-content:center;width:12px;height:12px;border-radius:50%;background:var(--teal);color:#fff;font-size:10px;line-height:1}

/* highlights */
.highlights{position:absolute;top:1780px;left:0;width:1200px;height:532px;background:linear-gradient(180deg,#1c2c46 0%,#23375a 55%,#17243a 100%)}
.accordion{position:absolute;left:86px;top:109px;width:676px}
.acc-head{height:51px;background:var(--teal);display:flex;align-items:center;color:#fff;font-size:16.5px;font-weight:500}
.acc-head .ic{width:56px;display:flex;justify-content:center}
.acc-head .title{flex:1}
.acc-head .toggle{width:44px;height:100%;border-left:1px solid rgba(255,255,255,.5);display:flex;align-items:center;justify-content:center;font-size:20px}
.acc-body{border:1px solid rgba(255,255,255,.7);border-top:none;height:129px;padding:14px 0 0 76px;list-style:none}
.acc-body li{font-size:13.5px;color:#fff;height:28.5px;line-height:28.5px}
.acc-body li::before{content:"⊕ ";font-size:12px}
.acc-closed{margin-top:11px}
.highlight-visual{position:absolute;left:789px;top:109px;width:325px;height:366px;background:radial-gradient(ellipse at 50% 40%,#2f6c8e 0%,#16304a 55%,#0c1828 100%)}

/* contact */
.contact{position:absolute;top:2312px;left:0;width:1200px;height:322px;background:linear-gradient(90deg,#b8e4ee,#cdebf2 60%,#a9dbe8)}
.contact-info{position:absolute;left:86px;top:0;width:327px;height:322px;background:var(--navy);color:#fff;font-size:15px;padding:55px 0 0 34px}
.info-row{display:flex;gap:12px;margin-bottom:22px;line-height:22px}
.info-row svg{flex:none;margin-top:4px}
.contact-form{position:absolute;left:474px;top:0;width:608px;height:322px}
.contact-form h2{position:absolute;top:56px;font-size:26px;font-weight:700;color:var(--ink)}
.field{position:absolute;border-bottom:1px solid #7fa9b6;font-size:12.5px;color:#4e6570;padding-bottom:6px}
.submit{position:absolute;left:0;top:246px;width:80px;height:33px;background:var(--teal);color:#fff;font-size:15px;font-weight:500;display:flex;align-items:center;justify-content:center}

/* footer */
.site-footer{position:absolute;top:2634px;left:0;width:1200px;height:57px;background:var(--navy-deep);color:#b9c2cc;font-size:13px}
.site-footer .copy{position:absolute;left:86px;top:20px}
.social{position:absolute;right:88px;top:20px;display:flex;gap:20px}
.social span{width:16px;height:16px;border-radius:50%;background:#b9c2cc}
</style>
</head>
<body>

<header class="site-header">
  <div class="brand"><span>Veritrace</span><span class="brand-dot"></span></div>
  <nav class="main-nav">
    <a class="active" href="#" style="left:452px">HOME</a>
    <a href="#" style="left:573px">FEATURES</a>
    <a href="#" style="left:725px">USE CASES</a>
    <a href="#" style="left:882px">HIGHLIGHTS</a>
    <a href="#" style="left:1045px">CONTACT</a>
  </nav>
</header>

<section class="hero">
  <div class="hero-art" role="img" aria-label="Dark visual of open hands beneath a glowing circuit-board brain chip"></div>
  <svg class="hero-arrow" style="left:16px" width="16" height="46" viewBox="0 0 16 46"><path d="M14 2 L2 23 L14 44" fill="none" stroke="#cfd6dc" stroke-width="2"/></svg>
  <svg class="hero-arrow" style="left:1168px" width="16" height="46" viewBox="0 0 16 46"><path d="M2 2 L14 23 L2 44" fill="none" stroke="#cfd6dc" stroke-width="2"/></svg>
  <h1 class="hero-title">PRODXYZ FOR GDPR</h1>
  <p class="hero-sub">Supports structured and unstructured data sources</p>
</section>

<h2 class="section-title" style="top:648px">MAIN FEATURES</h2>
<ul class="feature-list">
  <li class="feature-head">1.&nbsp; Detection of personal and sensitive data for GDPR Compliance</li>
  <li>
    <ul class="feature-detail">
      <li>in structural sources (e.g. SQL servers)</li>
      <li>in unstructured sources (e.g.: documents, e-mails, logs, data streams)</li>
      <li>in "noisy" content written in natural language (e.g.: containing errors or custom formats)</li>
      <li>built in ML models and rules for personal data used in Poland</li>
    </ul>
  </li>
  <li class="feature-item">2.&nbsp; Fast cataloging and classification of data and sources</li>
  <li class="feature-item">3.&nbsp; Unified data registry for RODO compliance fulfilment</li>
  <li class="feature-item">4.&nbsp; Management of consents and data access policies</li>
  <li class="feature-item">5.&nbsp; Customizable analytics and reporting</li>
  <li class="feature-item">6.&nbsp; Ability to integrates with tools for data anonymization or depersonalization</li>
  <li class="feature-item">7.&nbsp; Restful API for system management and integration</li>
</ul>
<div class="feature-visual"><div class="art" role="img" aria-label="Shield emblem marked GDPR ringed with stars, held up by a hand"></div></div>

<h2 class="section-title" style="top:1290px">USE CASES</h2>
<ul class="case-list">
  <li class="case" style="height:67px">
    <span class="case-icon"><svg width="30" height="30" viewBox="0 0 30 30" fill="none" stroke="#fff" stroke-width="2.5"><circle cx="15" cy="15" r="6"/><path d="M15 2v5M15 23v5M2 15h5M23 15h5M6 6l3.5 3.5M20.5 20.5L24 24M24 6l-3.5 3.5M9.5 20.5L6 24"/></svg></span>
    <span class="case-text">Internal audits and verification of the current status - in preparation for ensuring RODO compliance RODO</span>
  </li>
  <li class="case" style="height:64px">
    <span class="case-icon"><svg width="28" height="30" viewBox="0 0 28 30" fill="none" stroke="#fff" stroke-width="2"><ellipse cx="14" cy="6" rx="11" ry="4"/><path d="M3 6v18c0 2.2 4.9 4 11 4s11-1.8 11-4V6M3 12c0 2.2 4.9 4 11 4s11-1.8 11-4M3 18c0 2.2 4.9 4 11 4s11-1.8 11-4"/></svg></span>
    <span class="case-text">Cataloging sources that store sensitive data</span>
  </li>
  <li class="case" style="height:67px">
    <span class="case-icon"><svg width="28" height="30" viewBox="0 0 28 30" fill="none" stroke="#fff" stroke-width="2.5"><path d="M8 27V4M3 9l5-5 5 5M20 3v23M15 21l5 5 5-5"/></svg></span>
    <span class="case-text">Keeping the registry of personal data in order to implement rights to information, forgetfulness, data transfer</span>
  </li>
  <li class="case" style="height:66px">
    <span class="case-icon"><svg width="28" height="28" viewBox="0 0 28 28" fill="none" stroke="#fff" stroke-width="2"><path d="M3 3h18l4 4v18H3z"/><path d="M8 3v7h10V3M8 25v-9h12v9"/></svg></span>
    <span class="case-text">Continuous monitoring and classification of data</span>
  </li>
  <li class="case" style="height:68px">
    <span class="case-icon"><svg width="30" height="28" viewBox="0 0 30 28" fill="none" stroke="#fff" stroke-width="2"><path d="M15 2L28 26H2z"/><path d="M8 15h14M5 21h20M11 9h8"/></svg></span>
    <span class="case-text">Use collected the data to create additional business value, e.g.: <span class="tag" style="margin-left:10px">Classification of documents</span><span class="tag">Analysis of sentiment</span><br><span class="tag">Customer analytics for marketing</span><span class="tag">Fraud detection</span><span class="tag">Data governance</span></span>
  </li>
</ul>

<section class="highlights">
  <h2 class="section-title on-dark" style="top:30px">HIGHLIGHTS</h2>
  <div class="accordion">
    <div class="acc-head">
      <span class="ic"><svg width="22" height="24" viewBox="0 0 22 24" fill="none" stroke="#fff" stroke-width="1.8"><ellipse cx="11" cy="5" rx="9" ry="3.5"/><path d="M2 5v14c0 1.9 4 3.5 9 3.5s9-1.6 9-3.5V5M2 12c0 1.9 4 3.5 9 3.5s9-1.6 9-3.5"/></svg></span>
      <span class="title">Built in support for detection of Polish personal data</span>
      <span class="toggle">−</span>
    </div>
    <ul class="acc-body">
      <li>Sensitive data type (eg.:ID, name, address, etc.)</li>
      <li>Context of data occurrence</li>
      <li>Metadata describing the data source (e.g. system, table, author, etc.)</li>
      <li>Metadata describing the detection process</li>
    </ul>
    <div class="acc-head acc-closed">
      <span class="ic"><svg width="22" height="22" viewBox="0 0 22 22" fill="#fff"><path d="M10 2a9 9 0 1 0 9 10h-9z"/><path d="M12 0v10h10A10 10 0 0 0 12 0z"/></svg></span>
      <span class="title">High effectiveness of personal data detection by combining:</span>
      <span class="toggle">+</span>
    </div>
    <div class="acc-head acc-closed">
      <span class="ic"><svg width="22" height="24" viewBox="0 0 22 24" fill="none" stroke="#fff" stroke-width="1.8"><ellipse cx="9" cy="5" rx="7" ry="3"/><path d="M2 5v12c0 1.6 3 3 7 3M2 11c0 1.6 3 3 7 3"/><circle cx="16" cy="17" r="5"/></svg></span>
      <span class="title">Supports structured and unstructured data source</span>
      <span class="toggle">+</span>
    </div>
    <div class="acc-head acc-closed">
      <span class="ic"><svg width="24" height="22" viewBox="0 0 24 22" fill="#fff"><circle cx="12" cy="5" r="3.5"/><circle cx="4" cy="9" r="2.8"/><circle cx="20" cy="9" r="2.8"/><path d="M6 20c0-4 2.7-7 6-7s6 3 6 7zM0 20c0-3 1.6-5 4-5 1 0 1.5.3 2 .7L5 20zM24 20c0-3-1.6-5-4-5-1 0-1.5.3-2 .7l1 4.3z"/></svg></span>
      <span class="title">Ready for high performance processing</span>
      <span class="toggle">+</span>
    </div>
  </div>
  <div class="highlight-visual" role="img" aria-label="Finger touching a glowing circuit-board brain chip"></div>
</section>

<section class="contact">
  <div class="contact-info">
    <div class="info-row"><svg width="12" height="16" viewBox="0 0 12 16" fill="#fff"><path d="M6 0a6 6 0 0 0-6 6c0 4.5 6 10 6 10s6-5.5 6-10a6 6 0 0 0-6-6zm0 8.5A2.5 2.5 0 1 1 6 3.5a2.5 2.5 0 0 1 0 5z"/></svg><span>Veritrace Labs Sp. z o.o.<br>ul. Brzozowa 42<br>00-318 Lindow</span></div>
    <div class="info-row" style="margin-top:14px"><svg width="14" height="14" viewBox="0 0 14 14" fill="#fff"><path d="M3 0l3 3-1.5 2a8 8 0 0 0 4.5 4.5L11 8l3 3-2 3C6 14 0 8 0 2z"/></svg><span>0300-412-776</span></div>
    <div class="info-row" style="margin-top:14px"><svg width="15" height="12" viewBox="0 0 15 12" fill="#fff"><path d="M0 0h15v12H0z"/><path d="M0 0l7.5 6L15 0" fill="none" stroke="#1a2a44" stroke-width="1.5"/></svg><span>hello@veritrace-demo.com</span></div>
  </div>
  <form class="contact-form">
    <h2>CONTACT</h2>
    <div class="field" style="left:0;top:128px;width:285px">Enter Your Name</div>
    <div class="field" style="left:321px;top:124px;width:287px">Enter Your Email</div>
    <div class="field" style="left:0;top:193px;width:608px">Your Comment</div>
    <div class="submit">Submit</div>
  </form>
</section>

<footer class="site-footer">
  <span class="copy">© 2018 / All Rights Reserved</span>
  <div class="social"><span></span><span></span><span></span><span></span></div>
</footer>

</body>
</html>
```